business card for LWR pty ltd

We require a business card that stands out . I have included our company flyer and would like the services listed to be put on the card so when we Give out the cards to customers they have an idea of services we provide. need the winning design to be in editable photo shop format, editable iMac pages format or editable windows publisher format, so that I can enter in names, email addresses, phone numbers etc myself. I have included a pdf documents of info / items needed on the card to use as reference please.
Updates

need more submissions

Need extra days to review

Sick

Target Market(s)

new customers

Contact Information for Business Card

details are on attached business card requirements file

Requirements
Must have
• I have attached a list of must haves

```html
<!DOCTYPE html>
<html lang="en">
<head>
<meta charset="utf-8">
<title>LWR pty ltd – Business Card</title>
<link href="https://fonts.googleapis.com/css2?family=Quicksand:wght@400;500;700&display=swap" rel="stylesheet">
<style>
  :root {
    --page: #2a2a2c;
    --card-black: #0c0c0d;
    --card-grey: #1f1f21;
    --text-light: #e9e9ea;
    --text-soft: #c9c9cb;
    --gold: #b98a45;
    --gold-deep: #9a6c2f;
    --bullet: #c9923f;
    --photo-sand: #a68a6a;
    --photo-dark: #2b2724;
    --sky: #a9c6da;
  }
  * { margin: 0; padding: 0; box-sizing: border-box; }
  html, body { width: 1200px; height: 900px; overflow: hidden; }
  body {
    background: var(--page);
    font-family: "Quicksand", sans-serif;
    display: flex; flex-direction: column; align-items: center; justify-content: center;
    gap: 40px;
  }
  .card {
    width: 640px; height: 390px; border-radius: 26px; overflow: hidden;
    position: relative; background: var(--card-black);
    box-shadow: 0 18px 40px rgba(0,0,0,.45);
  }

  /* Front */
  .front-photo {
    position: absolute; left: 0; top: 0; width: 100%; height: 215px;
    background: linear-gradient(180deg, #050505 0%, #3a322b 45%, var(--photo-sand) 100%);
  }
  .front-photo::after {
    content: ""; position: absolute; inset: 0;
    background: linear-gradient(90deg, rgba(12,12,13,0) 55%, rgba(12,12,13,.85) 100%);
  }
  .brand-mark {
    position: absolute; right: 90px; top: 50px; z-index: 2;
    display: flex; align-items: center; gap: 14px;
    color: var(--text-light); font-weight: 700; font-size: 72px; letter-spacing: 2px;
  }
  .brand-mark .dot { width: 18px; height: 18px; border-radius: 50%; background: var(--text-light); }
  .front-band {
    position: absolute; left: 0; top: 200px; width: 100%; height: 190px;
    background: var(--card-grey); border-top: 2px solid #3a3a3d;
  }
  .person { position: absolute; top: 16px; width: 100%; text-align: center; color: var(--text-light); }
  .person-name { font-weight: 700; font-size: 24px; letter-spacing: 1.5px; }
  .person-title { font-size: 16px; letter-spacing: 1px; color: var(--text-soft); }
  .company {
    position: absolute; left: 40px; top: 92px; width: 250px; text-align: right;
    color: var(--text-soft); font-size: 15px; line-height: 1.35;
  }
  .company-name { font-weight: 700; font-size: 17px; color: var(--text-light); }
  .contact { position: absolute; left: 320px; top: 92px; list-style: none; color: var(--text-light); font-size: 15px; }
  .contact li { display: flex; align-items: center; gap: 8px; height: 24px; }
  .contact svg { width: 16px; height: 16px; flex: none; }

  /* Back */
  .back-photo {
    position: absolute; left: 0; top: 0; width: 250px; height: 300px;
    background: linear-gradient(180deg, var(--sky) 0%, #c9bba2 40%, #6f6a4a 70%, #3b3a30 100%);
  }
  .back-company {
    position: absolute; left: 22px; top: 16px; color: #111;
    font-weight: 700; font-size: 30px;
  }
  .services {
    position: absolute; left: 275px; top: 22px; list-style: none;
    color: var(--text-light); font-size: 17px; line-height: 22px;
  }
  .services li { position: relative; padding-left: 18px; }
  .services li::before {
    content: ""; position: absolute; left: 0; top: 8px; width: 8px; height: 8px;
    border-radius: 50%; background: var(--bullet);
  }
  .services li.cont { padding-left: 18px; }
  .services li.cont::before { display: none; }
  .offer-band {
    position: absolute; left: 0; bottom: 0; width: 100%; height: 82px;
    background: linear-gradient(90deg, var(--gold) 0%, var(--gold-deep) 100%);
    color: #fbeedc; font-size: 17px; line-height: 23px; letter-spacing: .5px;
    display: flex; align-items: center; padding: 0 36px; text-align: center;
  }
</style>
</head>
<body>

<section class="card card-front">
  <div class="front-photo" role="img" aria-label="Road train trucks parked on outback red dirt at dusk"></div>
  <div class="brand-mark"><span class="dot"></span>LWR</div>
  <div class="front-band">
    <div class="person">
      <div class="person-name">DANIEL REEVE</div>
      <div class="person-title">DIRECTOR</div>
    </div>
    <div class="company">
      <div class="company-name">LWR pty ltd</div>
      <div>Depot: Lot 114, Ridge Road Redhill</div>
    </div>
    <ul class="contact">
      <li>
        <svg viewBox="0 0 16 16"><circle cx="8" cy="8" r="7.5" fill="#e9e9ea"/><path d="M5 4.5c.6-.4 1.2 0 1.4.6l.4 1c.1.4-.1.7-.4.9.4.9 1.1 1.6 2 2 .2-.3.5-.5.9-.4l1 .4c.6.2 1 .8.6 1.4-.5.8-1.4 1-2.3.6C6.6 10.3 5.5 9.2 4.7 7.3c-.4-.9-.2-2.2.3-2.8z" fill="#1f1f21"/></svg>
        000 555 000
      </li>
      <li>
        <svg viewBox="0 0 16 16"><circle cx="8" cy="8" r="7.5" fill="#e9e9ea"/><rect x="4" y="5" width="8" height="6" rx="1" fill="none" stroke="#1f1f21" stroke-width="1.2"/><path d="M4.3 5.5 8 8.5l3.7-3" fill="none" stroke="#1f1f21" stroke-width="1.2"/></svg>
        info@lwrservices.com.au
      </li>
      <li>
        <svg viewBox="0 0 16 16"><circle cx="8" cy="8" r="7.5" fill="#e9e9ea"/><circle cx="8" cy="8" r="4.3" fill="none" stroke="#1f1f21" stroke-width="1.1"/><path d="M3.7 8h8.6M8 3.7c-2 2.4-2 6.2 0 8.6M8 3.7c2 2.4 2 6.2 0 8.6" fill="none" stroke="#1f1f21" stroke-width="1"/></svg>
        lwrservices.com.au
      </li>
    </ul>
  </div>
</section>

<section class="card card-back">
  <div class="back-photo" role="img" aria-label="Yellow road grader loaded on a drop deck trailer under a blue sky"></div>
  <div class="back-company">LWR pty ltd</div>
  <ul class="services">
    <li>Over size load/Hot Shot Loads</li>
    <li>Havy vehicle Recovery services</li>
    <li>Protable Water Deliveries</li>
    <li>Road Building/Maintenance</li>
    <li>Earthworks</li>
    <li>Sand &amp; Metal Supply &amp; Cartage</li>
    <li>Road Train Tippers</li>
    <li>Road Train Tankers</li>
    <li>Drop Deck Flat Tops</li>
    <li>Main Site accredited</li>
    <li class="cont">equipment &amp; Operators</li>
  </ul>
  <div class="offer-band">We offer a large range of services not listed so call us today for a personalised quote to suit your needs</div>
</section>

</body>
</html>
```